Personal Trainer and Corporate Health Business

I need a business card for a new company I'm starting in Australia called "Brisk Vitality Partners" I will be providing a Personal training service as well as corporate health in companies.
The service provided is to help promote an active and healthy lifstyle.
The design should communicate a healthy lifestyle and also the benefits that this can have on a personal level and in the corporate environment and the benefits that flow from that.

Target Market(s)

Members of the public and Corporate

Industry/Entity Type

Environment

Requirements
Must have
• Company logo attached
Look and feel fresh and modern

Tag line: "Actively promoting a healthier lifestyle"

Lewis Norgate
Managing Director

m: 0417 596 304
e: lewis@briskvitalitypartners.com.au

www.briskvitalitypartners.com.au
Nice to have
• Can be 1 or 2 sided

```html
<!DOCTYPE html>
<html lang="en">
<head>
<meta charset="utf-8">
<title>Brisk Vitality Partners – Business Card</title>
<link rel="stylesheet" href="https://fonts.googleapis.com/css2?family=Exo+2:wght@300;400&display=swap">
<style>
  :root {
    --backdrop: #e6e7e9;
    --card: #ffffff;
    --brand-blue: #1d5fb6;
    --name-blue: #4b8fd3;
    --soft-grey: #8c8f94;
    --logo-green: #8cc63f;
    --logo-blue: #1d5fb6;
  }
  * { box-sizing: border-box; margin: 0; padding: 0; }
  html, body {
    width: 1200px;
    height: 1200px;
    overflow: hidden;
    background: var(--backdrop);
  }
  .canvas {
    width: 1200px;
    height: 1200px;
    display: flex;
    align-items: center;
    justify-content: center;
  }
  .business-card {
    position: relative;
    width: 1000px;
    height: 570px;
    background: var(--card);
    box-shadow: 0 10px 30px rgba(0, 0, 0, 0.12);
    font-family: "Exo 2", sans-serif;
    font-weight: 300;
  }
  .brand-mark {
    position: absolute;
    left: 70px;
    top: 245px;
    display: flex;
    align-items: center;
    gap: 16px;
  }
  .brand-mark__dot {
    width: 34px;
    height: 34px;
    border-radius: 50%;
    background: var(--logo-green);
    flex: none;
  }
  .brand-mark__name {
    font-family: "Exo 2", sans-serif;
    font-weight: 400;
    font-size: 30px;
    line-height: 1.1;
    color: var(--logo-blue);
    width: 260px;
  }
  .card-details {
    position: absolute;
    left: 470px;
    top: 62px;
    width: 500px;
  }
  .company-name {
    font-weight: 300;
    font-size: 64px;
    line-height: 0.95;
    color: var(--brand-blue);
    letter-spacing: -0.5px;
  }
  .person-name {
    margin-top: 40px;
    font-size: 44px;
    line-height: 1;
    color: var(--name-blue);
  }
  .person-role {
    margin-top: 6px;
    font-size: 19px;
    color: var(--soft-grey);
  }
  .contact-list {
    margin-top: 34px;
    list-style: none;
    font-size: 21px;
    line-height: 1.5;
    color: var(--soft-grey);
  }
  .tagline {
    margin-top: 26px;
    font-size: 19px;
    color: var(--name-blue);
  }
</style>
</head>
<body>
  <main class="canvas">
    <article class="business-card">
      <div class="brand-mark">
        <span class="brand-mark__dot"></span>
        <span class="brand-mark__name">Brisk Vitality Partners</span>
      </div>
      <section class="card-details">
        <h1 class="company-name">brisk vitality<br>partners</h1>
        <p class="person-name">Lewis Norgate</p>
        <p class="person-role">managing director</p>
        <ul class="contact-list">
          <li>m: 0417 596 304</li>
          <li>e: lewis@briskvitalitypartners.com.au</li>
          <li>www.briskvitalitypartners.com.au</li>
        </ul>
        <p class="tagline">Actively promoting a healthier lifestyle</p>
      </section>
    </article>
  </main>
</body>
</html>
```